Organization and people consulting firm needs a website design

I need a website that promotes and explains the consulting service we will provide. The organization is called Halcrest Consulting Group. Our services include organization design, employee experience, change management, and executive coaching. I would like to see a simple clean and professional design, that reflects a modern and forward looking professional services company

Target Market(s)

Mid market and large companies

Industry/Entity Type

Management Consulting

Coding

Coded - Design and coding required

Number of Pages Required

5+ page

Font styles to use
Sans Serif

Colors

Designer to choose colors to be used in the design.

Requirements
Must have
• The following pages: Home, The Way We Work, What We Do, Our Founder, Insights, Contact.
• Search button.
• Hyper links (will be provided with main body text)
• Scrolling website with summaries at top level and links to more detail at lower level (like this website: brightmaple.example)
• Company logo (uploaded)
• I have text for each of the pages that I can upload once the basic design is done
Should not have
• No clutter, keep the design clean

```html
<!DOCTYPE html>
<html lang="en">
<head>
<meta charset="utf-8">
<title>Halcrest Consulting Group</title>
<link href="https://fonts.googleapis.com/css2?family=Roboto:wght@300;400;500&display=swap" rel="stylesheet">
<style>
:root{
  --brand:#e2184a;
  --brand-soft:#fbe6ec;
  --ink:#333333;
  --muted:#8a8a8a;
  --text:#777777;
  --white:#ffffff;
  --band:#f5f5f5;
  --band-dark:#ececec;
  --hero-dark:#2a2a2a;
  --hero-light:#bdbdbd;
}
*{margin:0;padding:0;box-sizing:border-box}
html,body{width:1200px;height:3947px;overflow:hidden}
body{font-family:'Roboto',Arial,sans-serif;color:var(--ink);background:var(--white);position:relative}
.site-header{height:95px;display:flex;align-items:center;padding:0 100px 0 100px;position:relative;background:var(--white)}
.brand{display:flex;align-items:center;gap:10px;color:var(--brand);font-size:22px;font-weight:400}
.brand-dot{width:22px;height:22px;border-radius:50%;background:var(--brand)}
.main-nav{position:absolute;left:479px;top:0;height:95px;display:flex;align-items:center;font-size:14px;color:var(--ink)}
.main-nav a{color:inherit;text-decoration:none;position:absolute;white-space:nowrap}
.main-nav a.active{color:var(--brand)}
.hero{position:absolute;top:95px;left:0;width:1200px;height:642px;overflow:hidden}
.hero-photo{position:absolute;inset:0;background:linear-gradient(100deg,#6f6f6f 0%,#c8c8c8 35%,#9a9a9a 60%,#3a3a3a 100%)}
.hero-curve{position:absolute;left:0;bottom:0;width:1200px;height:60px}
.hero-title{position:absolute;top:160px;width:100%;text-align:center;color:var(--white);font-size:62px;font-weight:300;letter-spacing:2px}
.hero-sub{position:absolute;top:238px;width:100%;text-align:center;color:var(--white);font-size:22px;font-weight:300;letter-spacing:8px}
.hero-arrow{position:absolute;top:278px;width:34px;height:34px}
.section{position:absolute;left:0;width:1200px;text-align:center}
.section-title{color:var(--brand);font-size:52px;font-weight:300}
.section-text{color:var(--text);font-size:21px;font-weight:300;line-height:34px;margin:0 auto}
.btn{display:inline-block;width:163px;height:51px;line-height:51px;background:var(--brand);color:var(--white);font-size:15px;text-decoration:none;text-transform:uppercase}
.way{top:737px;height:476px;background:var(--white)}
.services{top:1213px;height:592px;background:var(--band)}
.service{position:absolute;top:245px;width:240px;margin-left:-120px;text-align:center}
.service-icon{width:108px;height:108px;border-radius:50%;background:var(--white);border:1px solid #f0e3e6;margin:0 auto;display:flex;align-items:center;justify-content:center}
.service-icon.on{background:var(--brand);border-color:var(--brand)}
.service-name{margin-top:22px;font-size:19px;font-weight:400;color:var(--ink)}
.service.on .service-name{color:var(--brand)}
.service-desc{margin-top:10px;font-size:12px;line-height:19px;color:var(--muted);padding:0 22px}
.founder{top:1805px;height:874px;background:var(--white)}
.founder-ring{position:absolute;left:484px;top:329px;width:232px;height:232px;border-radius:50%;background:var(--brand-soft);display:flex;align-items:center;justify-content:center}
.founder-photo{width:184px;height:184px;border-radius:50%;background:radial-gradient(circle at 50% 40%,#6b5a55,#2b2220)}
.insights{top:2679px;height:569px;background:var(--band-dark)}
.contact{top:3248px;height:610px;background:var(--white)}
.contact-item{position:absolute;top:330px;display:flex;align-items:center;gap:18px;font-size:14px;color:var(--ink)}
.contact-icon{width:40px;height:40px;border-radius:50%;background:var(--white);box-shadow:0 0 0 1px #f1f1f1;display:flex;align-items:center;justify-content:center}
.site-footer{position:absolute;top:3858px;left:0;width:1200px;height:89px;background:var(--brand);color:var(--white);font-size:13px}
.site-footer .copy{position:absolute;top:36px;width:100%;text-align:center}
.site-footer .csr{position:absolute;top:36px;right:40px}
</style>
</head>
<body>
<header class="site-header">
  <div class="brand"><span class="brand-dot"></span>Halcrest Consulting Group</div>
  <nav class="main-nav">
    <a class="active" href="#" style="left:0">Home</a>
    <a href="#" style="left:76px">The Way We Work</a>
    <a href="#" style="left:219px">What We Do</a>
    <a href="#" style="left:330px">Our Founder</a>
    <a href="#" style="left:443px">Insights</a>
    <a href="#" style="left:528px">Contact</a>
    <a href="#" style="left:608px" aria-label="Search"><svg width="14" height="14" viewBox="0 0 14 14"><circle cx="6" cy="6" r="4.3" fill="none" stroke="#333" stroke-width="1.8"/><line x1="9" y1="9" x2="13" y2="13" stroke="#333" stroke-width="1.8"/></svg></a>
  </nav>
</header>

<section class="hero">
  <div class="hero-photo" role="img" aria-label="Black and white photo of business people walking through a glass office building"></div>
  <h1 class="hero-title">Halcrest Consulting Group</h1>
  <p class="hero-sub">We are organisation &amp; people consulting firm</p>
  <svg class="hero-arrow" style="left:26px" viewBox="0 0 34 34"><circle cx="17" cy="17" r="17" fill="rgba(255,255,255,.25)"/><polyline points="20,9 12,17 20,25" fill="none" stroke="#fff" stroke-width="2"/></svg>
  <svg class="hero-arrow" style="right:26px" viewBox="0 0 34 34"><polyline points="14,9 22,17 14,25" fill="none" stroke="#fff" stroke-width="2"/></svg>
  <svg class="hero-curve" viewBox="0 0 1200 60" preserveAspectRatio="none"><path d="M0 60 L0 42 Q600 -40 1200 42 L1200 60 Z" fill="#ffffff"/></svg>
</section>

<section class="section way">
  <h2 class="section-title" style="margin-top:22px">The Way We Work</h2>
  <p class="section-text" style="width:860px;margin-top:98px">Lorem ipsum dolor sit amet, consectetur adipiscing elit, sed do eiusmod tempor incididunt ut labore et dolore magna aliqua. Ut enim ad minim veniam, quis nostrud exercitation ullamco laboris nisi ut aliquip ex ea commodo consequat.</p>
  <a class="btn" href="#" style="margin-top:58px">Learn more</a>
</section>

<section class="section services">
  <h2 class="section-title" style="margin-top:78px">What We Do</h2>
  <div class="service" style="left:187px">
    <div class="service-icon"><svg width="50" height="44" viewBox="0 0 50 44" fill="none" stroke="#e2184a" stroke-width="1.6"><circle cx="25" cy="6" r="4"/><path d="M18 20 Q25 11 32 20"/><circle cx="10" cy="27" r="4"/><circle cx="25" cy="27" r="4"/><circle cx="40" cy="27" r="4"/><path d="M3 42 Q10 32 17 42M18 42 Q25 32 32 42M33 42 Q40 32 47 42"/></svg></div>
    <div class="service-name">Organisation design</div>
  </div>
  <div class="service" style="left:460px">
    <div class="service-icon"><svg width="50" height="40" viewBox="0 0 50 40" fill="none" stroke="#e2184a" stroke-width="1.6"><path d="M2 14 L12 8 L22 12 L30 8 L40 8 L48 14"/><path d="M12 8 L6 24 L18 34 Q22 36 26 32 L40 20"/><path d="M22 12 L16 18 Q19 22 24 18 L30 15"/><path d="M23 30 L18 26M28 27 L23 23"/></svg></div>
    <div class="service-name">Employee experience</div>
  </div>
  <div class="service on" style="left:734px">
    <div class="service-icon on"><svg width="52" height="46" viewBox="0 0 52 46" fill="none" stroke="#ffffff" stroke-width="1.6"><circle cx="26" cy="7" r="4"/><circle cx="8" cy="33" r="4"/><circle cx="44" cy="33" r="4"/><path d="M18 18 Q26 10 34 18M1 45 Q8 36 15 45M37 45 Q44 36 51 45"/><path d="M14 22 L10 26M38 22 L42 26M18 40 L34 40"/></svg></div>
    <div class="service-name">Change management</div>
    <p class="service-desc">Sed quia non numquam eius modi tempora incidunt ut labore et dolore magnam aliquam quaerat voluptatem.</p>
  </div>
  <div class="service" style="left:1008px">
    <div class="service-icon"><svg width="32" height="44" viewBox="0 0 32 44" fill="none" stroke="#e2184a" stroke-width="1.6"><path d="M9 30 Q2 24 2 16 A14 14 0 0 1 30 16 Q30 24 23 30 L23 34 L9 34 Z"/><path d="M10 38 L22 38M12 42 L20 42M12 20 L16 16 L20 20 M16 16 L16 30"/></svg></div>
    <div class="service-name">Executive coaching</div>
  </div>
</section>

<section class="section founder">
  <h2 class="section-title" style="margin-top:68px">Our Founder</h2>
  <p class="section-text" style="width:840px;margin-top:84px">At vero eos et accusamus et iusto odio dignissimos ducimus qui blanditiis praesentium voluptatum deleniti atque corrupti quos dolores et quas molestias excepturi sint occaecati cupiditate non provident, similique sunt in culpa qui officia deserunt mollitia animi.</p>
  <div class="founder-ring"><div class="founder-photo" role="img" aria-label="Portrait photo of the founder"></div></div>
  <div style="position:absolute;top:577px;width:100%;color:var(--brand);font-size:21px">Exercitationem Ullam</div>
  <div style="position:absolute;top:615px;width:100%;color:var(--muted);font-size:15px">Founder</div>
  <a class="btn" href="#" style="position:absolute;top:715px;left:518px">More about me</a>
</section>

<section class="section insights">
  <h2 class="section-title" style="margin-top:80px">Our Insights</h2>
  <p class="section-text" style="width:880px;margin-top:86px">But I must explain to you how all this mistaken idea of denouncing pleasure and praising pain was born and I will give you a complete account of the system, and expound the actual teachings of the great explorer of the truth.</p>
  <a class="btn" href="#" style="position:absolute;top:399px;left:518px">Learn more</a>
</section>

<section class="section contact">
  <h2 class="section-title" style="margin-top:76px">Contact Us</h2>
  <p style="position:absolute;top:212px;width:100%;font-size:15px;color:var(--muted);letter-spacing:1px">GET IN TOUCH WITH US AND SEE HOW WE CAN HELP</p>
  <p style="position:absolute;top:258px;width:100%;font-size:16px;color:var(--ink)">Daniel Halcrest, 48 Linden Hill Road, Westbrook, CT 06498, U.S.A</p>
  <div class="contact-item" style="left:138px"><span class="contact-icon"><svg width="14" height="14" viewBox="0 0 14 14"><path d="M3 1 L5 4 L4 6 Q6 9 8 10 L10 9 L13 11 L11 13 Q5 13 1 3 Z" fill="#e2184a"/></svg></span>+1-555-014-2290</div>
  <div class="contact-item" style="left:401px"><span class="contact-icon"><svg width="16" height="12" viewBox="0 0 16 12"><rect width="16" height="12" rx="1" fill="#e2184a"/><polyline points="1,1 8,7 15,1" fill="none" stroke="#fff" stroke-width="1.3"/></svg></span>daniel.halcrest@halcrestconsulting.example</div>
  <div class="contact-item" style="left:830px"><span class="contact-icon"><svg width="14" height="14" viewBox="0 0 14 14"><circle cx="7" cy="7" r="6.5" fill="#e2184a"/><path d="M1 7 H13 M7 1 Q3 7 7 13 Q11 7 7 1" fill="none" stroke="#fff" stroke-width="1"/></svg></span>halcrestconsulting.example</div>
  <a class="btn" href="#" style="position:absolute;top:455px;left:518px">Get in touch</a>
</section>

<footer class="site-footer">
  <div class="copy">© 2018 Halcrest Consulting Group. All right reserved. Term of Use</div>
  <div class="csr">CSR</div>
</footer>
</body>
</html>
```